Remodel Flyer for realtors

Ridgeline Builders

4"x 9" rack card front and back

www.BrambleworkHomes.example

555-318-4726

Let us fix what your home inspector finds!

Send us your inspection summary.

We are a licensed and Insured contractor.
CRC8071943

Serving
Dunmore County and Pelham Hollow

This flyer will sit in realtor offices for realtors to give to there buyers and sellers.

Target Market(s)

Realtors

Industry/Entity Type

Construction

Colors

Designer to choose colors to be used in the design.

```html
<!DOCTYPE html>
<html lang="en">
<head>
<meta charset="utf-8">
<title>Ridgeline Builders – Rack Card</title>
<link href="https://fonts.googleapis.com/css2?family=Oswald:wght@300;400;500;600&family=Montserrat:wght@400;500;600&display=swap" rel="stylesheet">
<style>
  :root {
    --orange: #f7931e;
    --charcoal: #58585a;
    --ink: #3d3d3f;
    --paper: #ffffff;
    --backdrop: #eceded;
  }
  * { box-sizing: border-box; margin: 0; padding: 0; }
  html, body { width: 1200px; height: 1063px; overflow: hidden; background: var(--backdrop); }
  .canvas { position: relative; width: 1200px; height: 1063px; }
  .card {
    position: absolute; top: 54px; width: 443px; height: 965px;
    background: var(--paper); overflow: hidden;
    box-shadow: -14px 6px 22px rgba(0,0,0,.16);
    font-family: "Montserrat", sans-serif;
  }
  .card--front { left: 74px; }
  .card--back { left: 674px; }
  .abs { position: absolute; }
  .photo { position: absolute; }

  /* front */
  .side-stripe { left: 0; top: 0; width: 43px; height: 569px; background: var(--orange); }
  .hero-photo { left: 50px; top: 0; width: 393px; height: 569px;
    background: linear-gradient(180deg, #d9c3a8 0%, #efe6dc 40%, #d8cab8 65%, #b88a5e 100%); }
  .headline-panel { left: 50px; top: 273px; width: 252px; height: 78px; background: rgba(255,255,255,.72); }
  .headline { left: 73px; top: 274px; font-family: "Oswald", sans-serif; line-height: 1.08; white-space: nowrap; }
  .headline__lead { display: block; font-weight: 300; font-size: 32px; color: var(--ink); }
  .headline__main { display: block; font-weight: 500; font-size: 35px; color: var(--orange); letter-spacing: -.3px; }
  .brand-box { left: 26px; top: 418px; width: 170px; height: 118px; background: var(--paper); padding: 6px; }
  .brand-box__frame { width: 100%; height: 100%; border: 3px solid var(--orange);
    display: flex; align-items: center; justify-content: center; }
  .brand-box__name { font-family: "Oswald", sans-serif; font-weight: 500; font-size: 17px; color: var(--ink); text-align: center; line-height: 1.2; letter-spacing: .5px; }
  .gallery-a { left: 0; top: 576px; width: 197px; height: 150px; background: linear-gradient(160deg, #e7c07a, #c8683a 70%, #8e3f22); }
  .gallery-b { left: 204px; top: 576px; width: 198px; height: 150px; background: linear-gradient(160deg, #6b6764, #2c2624 60%, #8b7060); }
  .gallery-block { left: 406px; top: 576px; width: 37px; height: 150px; background: var(--charcoal); }
  .cta { left: 0; width: 443px; text-align: center; font-family: "Oswald", sans-serif; line-height: 1; }
  .cta__lead { top: 754px; left: -4px; font-weight: 300; font-size: 37px; color: var(--ink); }
  .cta__main { top: 792px; font-weight: 600; font-size: 35px; color: var(--orange); }
  .contact { font-family: "Oswald", sans-serif; font-weight: 300; font-size: 21px; color: var(--ink); white-space: nowrap; }
  .contact strong { font-weight: 500; font-size: 27px; color: var(--orange); }
  .front-contact { left: 0; width: 443px; top: 857px; text-align: center; }
  .web { font-family: "Montserrat", sans-serif; font-weight: 600; font-size: 17px; letter-spacing: .3px; }
  .front-web { left: 0; width: 443px; top: 896px; text-align: center; color: var(--orange); }
  .front-band { left: 2px; top: 932px; width: 441px; height: 20px; background: var(--orange); }

  /* back */
  .top-band { left: 0; top: 0; width: 443px; height: 142px; background: var(--charcoal); }
  .mid-band { left: 0; top: 146px; width: 443px; height: 132px; background: var(--orange); }
  .tile { position: absolute; border: 4px solid var(--paper); }
  .tile--1 { left: 45px; top: 42px; width: 172px; height: 130px; background: linear-gradient(150deg, #f1f1ee, #b8b6b0 60%, #4a4a48); }
  .tile--2 { left: 225px; top: 42px; width: 174px; height: 130px; background: linear-gradient(150deg, #3b3634, #e7e3dd 55%, #c9a46b); }
  .tile--3 { left: 45px; top: 180px; width: 172px; height: 130px; background: linear-gradient(150deg, #d9d2bf, #8ea06a 45%, #c9b46c); }
  .tile--4 { left: 225px; top: 180px; width: 174px; height: 130px; background: linear-gradient(150deg, #f4f2ee, #c9b38e 50%, #2f2e2d); }
  .service-list { left: 0; width: 443px; top: 320px; text-align: center; font-family: "Oswald", sans-serif; font-weight: 500; font-size: 15.5px; color: var(--ink); white-space: nowrap; }
  .service-list .dot { display: inline-block; width: 4px; height: 4px; background: var(--orange); vertical-align: middle; margin: 0 4px; }
  .section-title { left: 0; width: 443px; top: 360px; text-align: center; font-family: "Oswald", sans-serif; font-size: 21px; color: var(--ink); font-weight: 500; }
  .section-title span { color: var(--orange); font-weight: 300; }
  .section-rule { left: 132px; top: 389px; width: 178px; height: 2px; background: var(--orange); }
  .services-sub { left: 0; width: 443px; top: 400px; text-align: center; font-weight: 600; font-size: 12px; color: var(--ink); }
  .services-body { left: 44px; width: 356px; top: 418px; text-align: center; font-size: 12.3px; line-height: 18.2px; color: #555; }
  .rule-top { left: 0; top: 555px; width: 443px; height: 3px; background: var(--orange); }
  .bedroom { left: 0; top: 558px; width: 443px; height: 176px; background: linear-gradient(180deg, #e9e3d6, #dcd2bf 45%, #8a7b66 100%); }
  .rule-bottom { left: 0; top: 734px; width: 443px; height: 3px; background: var(--orange); }
  .license { left: 66px; top: 742px; width: 310px; height: 54px; border: 2px solid #777; text-align: center; padding-top: 6px; }
  .license__note { font-size: 12.5px; color: #555; }
  .license__number { font-weight: 600; font-size: 23px; color: var(--orange); line-height: 1.2; }
  .serving { left: 0; width: 443px; top: 812px; text-align: center; font-size: 17px; color: var(--ink); }
  .serving__area { left: 0; width: 443px; top: 834px; text-align: center; font-size: 16.5px; font-weight: 600; color: var(--orange); }
  .back-band { left: 0; top: 874px; width: 443px; height: 64px; background: var(--orange); }
  .back-contact { left: 0; width: 443px; top: 877px; text-align: center; }
  .back-contact, .back-contact strong { color: var(--paper); }
  .back-web { left: 0; width: 443px; top: 913px; text-align: center; color: var(--paper); }
</style>
</head>
<body>
<div class="canvas">

  <section class="card card--front">
    <div class="abs side-stripe"></div>
    <div class="photo hero-photo" role="img" aria-label="Bright open-plan living room with curved staircase, cream sectional sofa and wood floor"></div>
    <div class="abs headline-panel"></div>
    <h1 class="abs headline">
      <span class="headline__lead">Let us fix what your</span>
      <span class="headline__main">HOME INSPECTOR FINDS!</span>
    </h1>
    <div class="abs brand-box">
      <div class="brand-box__frame">
        <div class="brand-box__name">RIDGELINE<br>BUILDERS</div>
      </div>
    </div>
    <div class="photo gallery-a" role="img" aria-label="Living room with fireplace and orange wood floor"></div>
    <div class="photo gallery-b" role="img" aria-label="Dark wood kitchen with island and pendant lights"></div>
    <div class="abs gallery-block"></div>

    <svg class="abs" style="left:0;top:0" width="443" height="965" aria-hidden="true">
      <polyline points="407,730 407,839 53,839" fill="none" stroke="#f7931e" stroke-width="2"/>
      <rect x="50" y="836" width="6" height="6" fill="#3d3d3f"/>
    </svg>
    <div class="abs cta cta__lead">SEND US YOUR</div>
    <div class="abs cta cta__main">INSPECTION SUMMARY</div>
    <div class="abs contact front-contact">CONTACT US <strong>555-318-4726</strong> OR VISIT US</div>
    <div class="abs web front-web">www.BrambleworkHomes.example</div>
    <div class="abs front-band"></div>
  </section>

  <section class="card card--back">
    <div class="abs top-band"></div>
    <div class="abs mid-band"></div>
    <div class="tile tile--1" role="img" aria-label="Modern bedroom with wardrobe wall"></div>
    <div class="tile tile--2" role="img" aria-label="Living room with ceiling fan and brick wall"></div>
    <div class="tile tile--3" role="img" aria-label="Lounge with media wall and garden view"></div>
    <div class="tile tile--4" role="img" aria-label="White kitchen with island and bar stools"></div>
    <div class="abs service-list"><span class="dot"></span> KITCHENS <span class="dot"></span> BATHROOMS <span class="dot"></span> ADDITIONS <span class="dot"></span> WHOLE HOMES</div>
    <h2 class="abs section-title"><span>OUR</span> SERVICES</h2>
    <div class="abs section-rule"></div>
    <div class="abs services-sub">Residential or Commercial</div>
    <p class="abs services-body">We've got all your needs covered: from residential remodels, to commercial damage repairs and everything in between. Don't hesitate to ask us a question or inquire as to why a certain process has to take place. All of our staff are friendly and knowledgeable because we know what it's like to be in your shoes. We want you to know just how special you and your project are to us.</p>
    <div class="abs rule-top"></div>
    <div class="photo bedroom" role="img" aria-label="Light bedroom with large bed, armchair and window"></div>
    <div class="abs rule-bottom"></div>
    <div class="abs license">
      <div class="license__note">We are a licensed and Insured contractor.</div>
      <div class="license__number">CRC8071943</div>
    </div>
    <div class="abs serving">SERVING</div>
    <div class="abs serving__area">Dunmore County and Pelham Hollow</div>
    <div class="abs back-band"></div>
    <div class="abs contact back-contact">CONTACT US <strong>555-318-4726</strong> OR VISIT US</div>
    <div class="abs web back-web">www.BrambleworkHomes.example</div>
  </section>

</div>
</body>
</html>
```